Stationery Design needed for logo design project

This project is linked to Logo: brand identity for modern furniture design studio..

Our company needs a Stationery Design. Please refer to our original project in the link above.

```html
<!DOCTYPE html>
<html lang="en">
<head>
<meta charset="utf-8">
<title>Ovalte Stationery</title>
<link href="https://fonts.googleapis.com/css2?family=Questrial&family=EB+Garamond:wght@400;600&display=swap" rel="stylesheet">
<style>
  :root{
    --backdrop:#a8a9b1;
    --folder:#2c2d31;
    --folder-inner:#26272b;
    --folder-edge:#1f2023;
    --paper:#ffffff;
    --paper-tint:#f2f3f7;
    --ink:#2a2a2e;
    --ink-soft:#55565c;
    --on-dark:#e6e6ea;
    --shadow:rgba(40,40,50,.35);
  }
  *{margin:0;padding:0;box-sizing:border-box}
  html,body{width:1200px;height:927px;overflow:hidden;background:var(--backdrop)}
  .canvas{position:relative;width:1200px;height:927px;font-family:"Questrial",sans-serif}
  .wordmark{font-family:"Questrial",sans-serif;font-weight:400;letter-spacing:.5px;line-height:1}

  /* open folder */
  .folder-open{position:absolute;left:200px;top:305px;width:725px;height:507px;background:var(--folder-inner);box-shadow:0 2px 6px var(--shadow)}
  .folder-open .spine{position:absolute;left:362px;top:0;width:1px;height:100%;background:var(--folder-edge)}
  .folder-open .left-pocket{position:absolute;left:290px;top:330px;width:72px;height:177px;background:var(--folder);border-top:1px solid var(--folder-edge)}
  .insert-sheet{position:absolute;left:377px;top:12px;width:333px;height:320px;background:var(--paper)}
  .right-pocket{position:absolute;left:363px;top:285px;width:362px;height:222px;background:var(--folder);border-top:1px solid #3a3b40}
  .card-slot{position:absolute;width:26px;height:26px;border-radius:50%;background:var(--folder-edge)}
  .slot-top{left:277px;top:8px}
  .slot-bottom{left:277px;top:151px;height:14px;border-radius:13px 13px 0 0}
  .pocket-address{position:absolute;right:56px;top:124px;text-align:right;color:var(--on-dark);font-size:5.4px;line-height:7px}

  /* closed folder cover */
  .folder-cover{position:absolute;left:158px;top:256px;width:335px;height:487px;background:var(--folder);box-shadow:1px 2px 6px var(--shadow)}
  .folder-cover .wordmark{position:absolute;left:137px;top:91px;font-size:24px;color:var(--on-dark)}
  .folder-cover .web{position:absolute;left:0;width:100%;top:441px;text-align:center;font-size:8px;color:#cfd0d5;letter-spacing:.3px}

  /* letterhead */
  .letterhead{position:absolute;left:670px;top:105px;width:335px;height:485px;background:linear-gradient(180deg,var(--paper),var(--paper-tint));box-shadow:0 2px 5px var(--shadow);color:var(--ink)}
  .letterhead .wordmark{position:absolute;left:54px;top:36px;font-size:20px;color:var(--ink-soft)}
  .letter-body{position:absolute;left:57px;top:122px;width:235px;font-family:"EB Garamond",serif;font-size:6.4px;line-height:8.6px}
  .subject{font-weight:600;font-size:6.8px}
  .dateline{position:absolute;right:0;top:0;text-align:right;font-size:6.8px}
  .greeting{margin-top:21px}
  .letter-body p{margin-top:9px}
  .signature{display:block;margin-top:18px;width:70px;height:34px;background:linear-gradient(90deg,#e9eaee,#dfe0e5);border-radius:3px}
  .signer{margin-top:4px;font-size:6.4px}
  .letter-footer{position:absolute;left:57px;top:445px;width:240px}
  .letter-footer .rule{width:128px;height:1px;background:#9c9da3}
  .letter-footer p{margin-top:5px;font-size:4.6px;line-height:7px;color:var(--ink-soft)}

  /* business cards */
  .card-front{position:absolute;left:843px;top:131px;width:145px;height:54px;background:var(--paper);box-shadow:0 1px 3px var(--shadow);color:var(--ink)}
  .card-front .wordmark{position:absolute;left:53px;top:10px;font-size:13px;color:var(--ink-soft)}
  .card-front .person{position:absolute;left:0;width:100%;top:30px;text-align:center;font-size:4.6px;letter-spacing:.4px}
  .card-front .role{position:absolute;left:0;width:100%;top:36px;text-align:center;font-size:3.4px;color:var(--ink-soft)}
  .card-front .contact{position:absolute;left:0;width:100%;top:42px;text-align:center;font-size:3.2px;line-height:4.4px;color:var(--ink-soft)}
  .card-back{position:absolute;left:953px;top:660px;width:52px;height:172px;background:var(--folder);box-shadow:1px 2px 4px var(--shadow)}
  .card-back .wordmark{position:absolute;left:26px;top:86px;transform:translate(-50%,-50%) rotate(90deg);font-size:15px;color:var(--on-dark)}
</style>
</head>
<body>
<main class="canvas">

  <section class="folder-open" aria-label="Presentation folder, open">
    <div class="spine"></div>
    <div class="left-pocket"></div>
    <div class="insert-sheet"></div>
    <div class="right-pocket">
      <div class="card-slot slot-top"></div>
      <div class="card-slot slot-bottom"></div>
      <p class="pocket-address">Atelier Norde<br>Rue des Lanternes<br>Lyon - Cedex 2207<br>France 69410</p>
    </div>
  </section>

  <section class="folder-cover" aria-label="Presentation folder cover">
    <div class="wordmark">ovalte</div>
    <div class="web">www.ovalte-studio.com</div>
  </section>

  <article class="letterhead">
    <div class="wordmark">ovalte</div>
    <div class="letter-body">
      <div class="subject">Demper sed feugiat felis hendrerit<br>ACCD Aenean scelerisque lorem aliquam.</div>
      <div class="dateline">18.11.2013<br>Lindmoor</div>
      <div class="greeting">Vitae gravida,</div>
      <p>Lorem ipsum dolor sit amet, consectetur adipiscing elit. Aenean aliquet, dui sodales blandit accumsan, lorem arcu volutpat orci, nec ultrices nulla neque id turpis. Integer non vulputate magna. Fusce nisl leo, pharetra non fringilla a, ornare a erat.</p>
      <p>Pellentesque gravida porttitor dolor sed congue. Morbi rhoncus purus eget nulla egestas laoreet. Morbi vehicula venenatis consectetur. Phasellus aliquam tellus sed elit consequat sodales. Cras et mauris metus. Lorem ipsum dolor sit amet, consectetur adipiscing elit. Fusce porta dui sed leo posuere aliquet.</p>
      <p>Donec sed odio sit amet nisi dapibus consectetur ut sed lorem. In porttitor, nisi eu egestas fringilla, purus nulla adipiscing nulla, eget sagittis nisi augue nec odio. Ut convallis malesuada mauris eu pellentesque. Donec faucibus pellentesque volutpat.</p>
      <p>Etiam placerat, nulla nec adipiscing accumsan, arcu dolor aliquet nisi, vitae gravida ipsum arcu non sapien. Nulla placerat nibh vel orci porttitor at quam lacus. Donec iaculis ornare nunc in lobortis. Vestibulum semper tincidunt. Curabitur mollis nunc non lorem posuere pellentesque. Etiam porttitor vulputate feugiat. Vivamus commodo diam non.</p>
      <span class="signature" role="img" aria-label="Handwritten signature"></span>
      <div class="signer">Jonas Weller<br>Managing Director</div>
    </div>
    <footer class="letter-footer">
      <div class="rule"></div>
      <p>Unit 4, 88 Kestrel Rd, Lindmoor 5120 · P: (03) 5510 7724<br>P: (03) 5510 7724 · E: hello@ovalte-studio.com · www.ovalte-studio.com</p>
    </footer>
  </article>

  <section class="card-front" aria-label="Business card, front">
    <div class="wordmark">ovalte</div>
    <div class="person">MARA TELLINGS</div>
    <div class="role">Studio Director</div>
    <div class="contact">Unit 4, 88 Kestrel Rd, Lindmoor 5120 · P: (03) 5510 7724<br>E: hello@ovalte-studio.com · www.ovalte-studio.com</div>
  </section>

  <section class="card-back" aria-label="Business card, back">
    <div class="wordmark">ovalte</div>
  </section>

</main>
</body>
</html>
```